Brightfield Steel Depot (Metal Roofing Manufacturing and Supply) needs a billboard design

We need a billboard design for for our metal roofing manufacturing company in Sarasota FL, Brightfield Steel Depot Inc. You can visit our website www.brightfieldsteeldepot-example.com for more info about our company. We located are off Exit 210 on I 75- 482 Pinegrove Rd. Sarasota 34019
The billboard will be on I75 north of our office

I have a design that I am interested in but waiting on minor corrections from designer

```html
<!DOCTYPE html>
<html lang="en">
<head>
<meta charset="utf-8">
<title>Brightfield Steel Depot – Billboard</title>
<link href="https://fonts.googleapis.com/css2?family=Bebas+Neue&family=Poppins:wght@600;700&family=Roboto:wght@400;500&family=Roboto+Condensed:wght@500&display=swap" rel="stylesheet">
<style>
  :root{
    --brand-blue:#33549f;
    --logo-blue:#2a3f93;
    --brand-yellow:#ecca1f;
    --ink:#1f1f1f;
    --paper:#ffffff;
    --sky:#eef3f8;
    --roof:#4a78a8;
  }
  html,body{margin:0;padding:0;width:900px;height:1200px;overflow:hidden;background:var(--paper);}
  .canvas{position:relative;width:900px;height:1200px;}
  .billboard{
    position:absolute;left:30px;top:477px;
    width:1162px;height:340px;
    transform:scale(0.7229);transform-origin:0 0;
    box-shadow:2px 3px 4px rgba(0,0,0,.35);
    overflow:hidden;
  }
  .billboard__shapes{position:absolute;inset:0;width:1162px;height:340px;}
  .brand-name{
    position:absolute;left:56px;top:60px;margin:0;white-space:nowrap;
    font-family:"Roboto",sans-serif;font-weight:500;font-size:29px;
    color:var(--logo-blue);letter-spacing:-.2px;
  }
  .brand-mark{
    position:absolute;left:42px;top:34px;width:26px;height:26px;
    background:var(--brand-yellow);border-radius:50%;
  }
  .headline{position:absolute;right:37px;top:36px;margin:0;text-align:right;white-space:nowrap;}
  .headline__lead{
    display:block;font-family:"Roboto",sans-serif;font-weight:400;
    font-size:44px;line-height:46px;color:var(--paper);letter-spacing:.3px;
  }
  .headline__main{
    display:block;font-family:"Bebas Neue",sans-serif;font-size:92px;
    line-height:80px;color:var(--brand-yellow);letter-spacing:.5px;
  }
  .tagline{
    position:absolute;right:37px;top:206px;margin:0;text-align:right;white-space:nowrap;
    font-family:"Roboto Condensed",sans-serif;font-weight:500;font-size:16.5px;
    line-height:20px;color:var(--ink);
  }
  .contact{
    position:absolute;left:552px;right:37px;top:265px;height:75px;
    display:flex;align-items:center;justify-content:flex-end;gap:10px;
    font-family:"Poppins",sans-serif;color:var(--ink);white-space:nowrap;
  }
  .contact__phone{font-weight:700;font-size:32px;line-height:1;letter-spacing:-.3px;}
  .contact__divider{flex:none;width:2px;height:30px;background:var(--ink);margin:0 8px;}
  .contact__web{font-weight:600;font-size:10.5px;line-height:1;}
  .icon{display:block;flex:none;}
</style>
</head>
<body>
<div class="canvas">
  <section class="billboard" aria-label="Brightfield Steel Depot billboard">
    <svg class="billboard__shapes" viewBox="0 0 1162 340">
      <defs>
        <linearGradient id="photoTone" x1="0" y1="0" x2="0.3" y2="1">
          <stop offset="0" stop-color="var(--sky)"/>
          <stop offset="0.38" stop-color="#e4ecf4"/>
          <stop offset="0.45" stop-color="#5d88b6"/>
          <stop offset="1" stop-color="var(--roof)"/>
        </linearGradient>
      </defs>
      <rect x="0" y="0" width="560" height="340" fill="url(#photoTone)" role="img"
        aria-label="Photo of a roofer in hard hat and safety vest installing blue metal roof panels"/>
      <polygon points="415,0 1162,0 1162,340 530,340" fill="var(--brand-blue)"/>
      <polygon points="437,0 452,0 522,190 507,190" fill="var(--brand-yellow)"/>
      <polygon points="508,190 1162,190 1162,265 533,265" fill="var(--paper)"/>
      <polygon points="533,265 1162,265 1162,340 558,340" fill="var(--brand-yellow)"/>
    </svg>

    <span class="brand-mark" aria-hidden="true"></span>
    <p class="brand-name">Brightfield Steel Depot</p>

    <h1 class="headline">
      <span class="headline__lead">FLORIDA'S PREMIER METAL</span>
      <span class="headline__main">ROOF MANUFACTURER</span>
    </h1>

    <p class="tagline">Lorem Ipsum is simply dummy text of the printing and typesetting industry<br>the printing and typesetting industry.</p>

    <div class="contact">
      <svg class="icon" width="30" height="30" viewBox="0 0 24 24" aria-hidden="true">
        <path fill="var(--brand-blue)" d="M6.6 10.8a15.1 15.1 0 0 0 6.6 6.6l2.2-2.2c.3-.3.7-.4 1-.2 1.1.4 2.3.6 3.6.6.6 0 1 .4 1 1V20c0 .6-.4 1-1 1A17 17 0 0 1 3 4c0-.6.4-1 1-1h3.5c.6 0 1 .4 1 1 0 1.3.2 2.5.6 3.6.1.3 0 .7-.2 1z"/>
        <path fill="none" stroke="var(--brand-blue)" stroke-width="1.6" d="M14 3.5a7 7 0 0 1 6.5 6.5M14 7a3.5 3.5 0 0 1 3 3"/>
      </svg>
      <span class="contact__phone">941-555-0187</span>
      <span class="contact__divider" aria-hidden="true"></span>
      <svg class="icon" width="15" height="15" viewBox="0 0 20 20" aria-hidden="true">
        <g fill="none" stroke="var(--brand-blue)" stroke-width="1.6">
          <circle cx="10" cy="10" r="8.5"/>
          <ellipse cx="10" cy="10" rx="3.8" ry="8.5"/>
          <path d="M1.5 10h17M3 5.5h14M3 14.5h14M10 1.5v17"/>
        </g>
      </svg>
      <span class="contact__web">www.brightfieldsteeldepot-example.com</span>
    </div>
  </section>
</div>
</body>
</html>
```